Beach Polo Event Flyer

The project consists of a flyer for a beach polo event that will occur on August 30 and 31

The flyer should contain the event details in spanish:
IV MARENQUA SHORE RIDING CUP
Hotel Varlowe
Agosto 30 y 31 2014
Horario: 2pm a 6pm
(Varlowe Logo)

Also contact info below:
info@brisadelvarclub.example
www.brisadelvarclub.example

A Space should be left on the bottom for us to add the sponsor logos when we have them.

The general idea is to do a flyer that looks elegant, inviting, inspired on the beach and the caribbean and shows the beauty of the sport and the beach.

I am attaching the flyer that a friend made that we DO NOT LIKE and some flyers from events in other parts of the world that we do like.
Also attached you will find the BRISADEL VAR CLUB logo which should go somewhere in the flyer. We are also attaching pictures from the past event in case you would need to use them.
We are open for any questions

```html
<!DOCTYPE html>
<html lang="es">
<head>
<meta charset="utf-8">
<title>IV Marenqua Shore Riding Cup</title>
<link href="https://fonts.googleapis.com/css2?family=Playfair+Display:wght@400;700;900&family=Cinzel:wght@400;700&display=swap" rel="stylesheet">
<style>
  :root {
    --orange: #f4a21e;
    --orange-deep: #e98c12;
    --black: #111111;
    --white: #ffffff;
    --band: rgba(255, 255, 255, 0.88);
    --maroon: #7a1c3a;
    --red: #d4182c;
    --ink: #2a1a14;
    --horse-dark: #4a2a18;
    --horse-mid: #8a5430;
  }
  html, body {
    margin: 0;
    padding: 0;
    width: 822px;
    height: 1200px;
    overflow: hidden;
    background: var(--orange);
  }
  .flyer {
    position: relative;
    width: 822px;
    height: 1200px;
    overflow: hidden;
    background: radial-gradient(ellipse at 60% 40%, var(--orange) 0%, var(--orange-deep) 100%);
    font-family: "Playfair Display", Georgia, serif;
  }
  .hero-photo {
    position: absolute;
    left: 0;
    top: 0;
    width: 822px;
    height: 760px;
  }
  .club-corner {
    position: absolute;
    left: 0;
    top: 0;
    width: 400px;
    height: 430px;
  }
  .club-mark {
    position: absolute;
    left: 40px;
    top: 48px;
    width: 200px;
    text-align: center;
    color: var(--white);
    font-family: "Cinzel", Georgia, serif;
    font-weight: 400;
  }
  .club-mark .dot {
    display: block;
    width: 58px;
    height: 58px;
    margin: 0 auto 22px;
    border: 3px solid var(--white);
    border-radius: 50%;
  }
  .club-mark .name {
    font-size: 27px;
    line-height: 1.15;
    letter-spacing: 1px;
  }
  .event-block {
    position: absolute;
    left: 215px;
    top: 650px;
    width: 760px;
    transform: rotate(-8deg);
    transform-origin: left top;
  }
  .band {
    display: block;
    box-sizing: border-box;
    width: 100%;
    background: var(--band);
    padding: 4px 0 4px 16px;
    margin-bottom: 7px;
    line-height: 1.05;
    white-space: nowrap;
    text-transform: uppercase;
  }
  .date-line {
    color: var(--maroon);
    font-size: 50px;
    font-weight: 400;
  }
  .title-line {
    color: var(--ink);
    font-size: 46px;
    font-weight: 900;
  }
  .days-line {
    color: var(--red);
    font-size: 58px;
    font-weight: 900;
    text-align: right;
    padding-right: 190px;
  }
  .hours-line {
    color: var(--maroon);
    font-size: 42px;
    font-weight: 400;
    text-align: right;
    padding-right: 190px;
  }
  .hotel-mark {
    position: absolute;
    left: 630px;
    top: 990px;
    width: 160px;
    text-align: center;
    color: var(--maroon);
    font-weight: 700;
  }
  .hotel-mark .dot {
    display: block;
    width: 40px;
    height: 40px;
    margin: 0 auto 6px;
    border-radius: 50%;
    background: var(--maroon);
  }
  .hotel-mark .name {
    font-size: 46px;
    line-height: 1;
  }
  .contact {
    position: absolute;
    right: 38px;
    top: 1118px;
    text-align: right;
    color: var(--maroon);
    font-size: 20px;
    line-height: 1.45;
  }
</style>
</head>
<body>
<main class="flyer">
  <svg class="hero-photo" viewBox="0 0 822 760" role="img" aria-label="Photograph of a polo player in white riding a chestnut horse mid-gallop, mallet swinging">
    <defs>
      <radialGradient id="horseTone" cx="0.6" cy="0.45" r="0.6">
        <stop offset="0" stop-color="var(--horse-mid)"/>
        <stop offset="0.6" stop-color="var(--horse-dark)" stop-opacity="0.75"/>
        <stop offset="1" stop-color="var(--orange-deep)" stop-opacity="0"/>
      </radialGradient>
    </defs>
    <rect x="180" y="0" width="642" height="760" fill="url(#horseTone)"/>
  </svg>

  <svg class="club-corner" viewBox="0 0 400 430" aria-hidden="true">
    <polygon points="0,0 400,0 0,430" fill="var(--black)"/>
  </svg>

  <div class="club-mark">
    <span class="dot"></span>
    <span class="name">BRISADEL VAR<br>CLUB</span>
  </div>

  <section class="event-block">
    <span class="band date-line">Agosto 2014</span>
    <span class="band title-line">IV Marenqua</span>
    <span class="band title-line">Shore Riding Cup</span>
    <span class="band days-line">30-31</span>
    <span class="band hours-line">2pm a 6pm</span>
  </section>

  <div class="hotel-mark">
    <span class="dot"></span>
    <span class="name">Varlowe</span>
  </div>

  <address class="contact">
    info@brisadelvarclub.example<br>
    www.brisadelvarclub.example
  </address>
</main>
</body>
</html>
```